Picture Ads

We need some banner ads for our home business opportunity, we are evolving from text to picture ads. I have added some examples of what other distributors are using. We are looking for something really eye catching with some good key words and nice bright colours and to include our photo (attached)
Key words to include:
Booming online business
Personal Development and Leadership Industry
Earn an executive income from home
Simple 3 step system
Make up to $5,000 per sale
Not MLM
The size needs to be: 1000 x 35 pixels
13.9 x 4.75 Inches
35.3 x 11.1 cm
I think different platforms accept different sizes, not too familiar with it yet, any guidance welcome. I've clicked project for 2 days if that is to prioritise the order?
Many thanks,
Maren

Industry/Entity Type

Business

```html
<!DOCTYPE html>
<html lang="en">
<head>
<meta charset="utf-8">
<title>Booming Online Business Banner</title>
<link href="https://fonts.googleapis.com/css2?family=Arimo:wght@700&display=swap" rel="stylesheet">
<style>
  :root {
    --pink: #d81b5e;
    --charcoal: #3a3a3a;
    --ink: #111111;
    --grey: #d3d3d3;
    --white: #ffffff;
  }
  html, body {
    margin: 0;
    padding: 0;
    width: 1200px;
    height: 410px;
    overflow: hidden;
    background: var(--grey);
  }
  .banner {
    position: relative;
    width: 1200px;
    height: 410px;
    font-family: "Arimo", Arial, Helvetica, sans-serif;
    font-weight: 700;
    color: var(--white);
    text-transform: uppercase;
    overflow: hidden;
  }
  .shapes {
    position: absolute;
    left: 0;
    top: 0;
  }
  .text {
    position: absolute;
    margin: 0;
    line-height: 1;
    white-space: nowrap;
  }
  .headline-big { left: 10px; top: 6px; font-size: 72px; letter-spacing: -3px; }
  .headline-small { left: 12px; top: 72px; font-size: 35px; letter-spacing: 0.2px; }
  .industry { left: 26px; top: 161px; font-size: 43px; line-height: 48px; }
  .names { left: 590px; top: 20px; font-size: 20px; letter-spacing: 0.2px; }
  .perk { left: 451px; font-size: 40px; letter-spacing: -1px; }
  .perk-1 { top: 89px; }
  .perk-2 { top: 137px; }
  .perk-3 { top: 211px; }
  .perk-4 { top: 281px; }
  .offer-lead { left: 768px; top: 293px; font-size: 56px; line-height: 54px; }
  .offer-currency { left: 942px; top: 300px; font-size: 28px; }
  .offer-amount { left: 968px; top: 294px; font-size: 79px; letter-spacing: -1px; }
  .offer-tail { left: 966px; top: 370px; font-size: 37px; letter-spacing: 0.5px; }
</style>
</head>
<body>
<div class="banner">
  <svg class="shapes" width="1200" height="410" viewBox="0 0 1200 410">
    <defs>
      <linearGradient id="portrait-tone" x1="0" y1="0" x2="1" y2="1">
        <stop offset="0" stop-color="#5a3a2c"/>
        <stop offset="0.5" stop-color="#b07a5c"/>
        <stop offset="1" stop-color="#3a241c"/>
      </linearGradient>
    </defs>
    <rect width="1200" height="410" fill="var(--grey)"/>
    <polygon class="band-pink" points="0,142 324,142 384,48 1200,48 1200,348 0,348" fill="var(--pink)"/>
    <polygon class="title-block" points="0,0 378,0 384,48 324,142 0,142" fill="var(--charcoal)"/>
    <polygon class="title-notch" points="384,48 406,4 428,48" fill="var(--ink)"/>
    <polygon class="names-tab" points="582,0 948,0 948,48 562,48" fill="var(--charcoal)"/>
    <polygon class="names-notch" points="546,48 570,8 594,48" fill="var(--ink)"/>
    <line class="divider" x1="428" y1="70" x2="428" y2="326" stroke="var(--white)" stroke-width="2.5"/>
    <circle cx="428" cy="70" r="5" fill="var(--white)"/>
    <circle cx="428" cy="326" r="5" fill="var(--white)"/>
    <polygon class="offer-notch" points="666,348 726,348 696,404" fill="var(--ink)"/>
    <polygon class="offer-block" points="792,274 1200,274 1200,410 700,410" fill="var(--charcoal)"/>
    <rect class="portrait-frame" x="946" y="0" width="254" height="268" fill="var(--charcoal)"/>
    <rect class="portrait" x="950" y="4" width="246" height="260" fill="url(#portrait-tone)" role="img" aria-label="Photo of the two business owners smiling together"/>
  </svg>

  <p class="text headline-big">Booming</p>
  <p class="text headline-small">Online Business</p>
  <p class="text industry">Personal<br>Development<br>and Leadership<br>Industry</p>
  <p class="text names">Maren and Rosalind Hartley</p>
  <p class="text perk perk-1">Earn an Executive</p>
  <p class="text perk perk-2">Income from Home</p>
  <p class="text perk perk-3">Simple 3 Step System</p>
  <p class="text perk perk-4">Not MLM</p>
  <p class="text offer-lead">Make<br>Up to</p>
  <p class="text offer-currency">$</p>
  <p class="text offer-amount">5,000</p>
  <p class="text offer-tail">Per Sale</p>
</div>
</body>
</html>
```